Volren Goods Ltd Stationery Design Project

hi we need to design business cards, letter head, complimentary slips, scribble pads, note pads, envelopes for volren goods ltd.

please see business cards details

Kelvin Obutu

P.O Box 41873 -00312 Nairobi - Kenya
Tel: +254-733-218-904
Email: volrengoods@mailvexo.com

company name should appear on all stationery : Volren Goods Ltd

Industry/Entity Type

Business

Requirements
Must have
• kindly stick to colours in the logo

```html
<!DOCTYPE html>
<html lang="en">
<head>
<meta charset="UTF-8">
<title>Volren Goods Ltd – Envelope</title>
<link rel="stylesheet" href="https://fonts.googleapis.com/css2?family=Quicksand:wght@500;700&display=swap">
<style>
  :root {
    --paper: #e6e7e8;
    --brand-navy: #2b3a8f;
    --ink: #1d1d1f;
    --rule: #7a7a7c;
  }
  * { margin: 0; padding: 0; box-sizing: border-box; }
  html, body {
    width: 1200px;
    height: 877px;
    overflow: hidden;
    background: var(--paper);
  }
  .envelope {
    position: relative;
    width: 1200px;
    height: 877px;
    background: var(--paper);
    font-family: "Quicksand", sans-serif;
    color: var(--ink);
  }
  .brand-name {
    position: absolute;
    left: 31px;
    top: 26px;
    width: 244px;
    height: 171px;
    display: flex;
    align-items: center;
    justify-content: center;
    font-weight: 700;
    font-size: 30px;
    color: var(--brand-navy);
    white-space: nowrap;
  }
  .sender {
    position: absolute;
    left: 312px;
    top: 30px;
    font-style: normal;
  }
  .sender__company {
    font-weight: 700;
    font-size: 30px;
    line-height: 38px;
    color: var(--brand-navy);
    margin-bottom: 6px;
  }
  .sender__line {
    font-weight: 500;
    font-size: 20px;
    line-height: 32px;
  }
  .recipient {
    position: absolute;
    left: 702px;
    top: 526px;
    width: 498px;
    height: 240px;
  }
  .recipient__label {
    position: absolute;
    left: 0;
    top: 0;
    font-weight: 500;
    font-size: 20px;
  }
  .recipient__rule {
    position: absolute;
    left: 44px;
    right: 0;
    height: 0;
    border-top: 2px solid var(--rule);
  }
</style>
</head>
<body>
  <main class="envelope">
    <div class="brand-name">Volren Goods</div>

    <address class="sender">
      <div class="sender__company">Volren Goods Ltd</div>
      <div class="sender__line">Nairobi - Kenya</div>
      <div class="sender__line">P.O Box 41873 -00312</div>
      <div class="sender__line">Tel: +254-733-218-904</div>
      <div class="sender__line">Email: volrengoods@mailvexo.com</div>
    </address>

    <section class="recipient" aria-label="Recipient address">
      <span class="recipient__label">To:</span>
      <span class="recipient__rule" style="top: 22px;"></span>
      <span class="recipient__rule" style="top: 63px;"></span>
      <span class="recipient__rule" style="top: 104px;"></span>
      <span class="recipient__rule" style="top: 145px;"></span>
      <span class="recipient__rule" style="top: 186px;"></span>
      <span class="recipient__rule" style="top: 227px;"></span>
    </section>
  </main>
</body>
</html>
```